Laboratory and geotechnical service provider needs Word template

We require a new Word Template for our business. We are looking for a modern, business-like format. We typically generate reports such as management plans, business plans, method statements, technical reports. These reports cover generally between 5 and 30 pages, but sometimes up to 500 pages including the appendices.

Lab reports have their own formats and are not parts of this scope.

Target Market(s)

We report to Clients such as construction industry contractors, governmental departments and engineering consultants.

Industry/Entity Type

Technical Service

Colors

Designer to choose colors to be used in the design.

Requirements
Must have
• The report needs a fancy cover page with a title field, subtitle, project field, client name field, reference number field. Photo/graphics as background on cover. Second page needs a revision table for document control. Table of contents up to 2 levels. Appendices to be part of TOC. Report first page with custom headings for body text, titles, subtitles, headings 1, 2, 3, etc. Include a table with caption, figure with caption, bullet list, numbered list. Appendix page. Please use fonts consistently, choose a common, but professional, modern font.
Nice to have
• We traditionally use black and yellow as company colours. Please visit our company page www.tarnvalecores.com.
Should not have
• The two attached word documents is what we use now for your information, we are looking for something better!

```html
<!DOCTYPE html>
<html lang="en">
<head>
<meta charset="utf-8">
<title>Tarnvale Cores – Report Template</title>
<link href="https://fonts.googleapis.com/css2?family=Source+Sans+3:wght@400;600;700&display=swap" rel="stylesheet">
<style>
:root{
  --yellow:#fbed19;
  --yellow-soft:#fcf59c;
  --ink:#231f20;
  --text:#3a3a3a;
  --paper:#ffffff;
  --desk:#ececec;
  --rule:#cfcfcf;
  --ghost:#efefef;
}
*{box-sizing:border-box;margin:0;padding:0}
html,body{width:1200px;height:1133px;overflow:hidden}
body{background:var(--desk);font-family:"Source Sans 3",Arial,sans-serif;color:var(--text);position:relative}
.page{position:absolute;width:616px;height:869px;background:var(--paper);transform:scale(.604);transform-origin:0 0;overflow:hidden;box-shadow:0 6px 22px rgba(0,0,0,.28)}
.p1{left:23px;top:27px}.p2{left:416px;top:27px}.p3{left:808px;top:27px}
.p4{left:23px;top:581px}.p5{left:416px;top:581px}.p6{left:808px;top:581px}

/* inner page chrome */
.edge{position:absolute;left:0;top:0;width:10px;height:869px}
.brand{position:absolute;right:18px;top:20px;text-align:left;font-weight:700;color:var(--ink);font-size:19px;line-height:18px;letter-spacing:.5px}
.brand span{display:block;padding-left:14px}
.footer-rule{position:absolute;left:10px;width:572px;top:853px;height:3px;background:var(--ink)}
.folio{position:absolute;right:16px;top:843px;font-size:11px;font-weight:700;color:var(--ink)}
.pill{position:absolute;left:24px;right:18px;height:40px;border-radius:20px;background:var(--yellow);display:flex;align-items:center;justify-content:center;font-weight:700;font-size:22px;color:var(--ink)}
.pill.dark{background:var(--ink);color:#fff}
.pill.numbered{justify-content:flex-start;padding-left:14px}
.pill .num{font-size:28px;padding-right:8px;border-right:2px solid var(--ink);margin-right:10px;line-height:34px}

/* cover */
.cover{background:var(--ink)}
.cover-shape{position:absolute;inset:0}
.cover-top{background:var(--yellow);clip-path:polygon(0 0,327px 0,197px 265px,0 265px)}
.cover-bottom{background:var(--yellow);clip-path:polygon(0 805px,215px 805px,252px 725px,355px 869px,0 869px)}
.cover-photo{background:linear-gradient(120deg,#d9dbde 0%,#9ea3a8 45%,#e8c52a 70%,#6d6f72 100%);clip-path:polygon(0 287px,253px 287px,336px 537px,253px 800px,0 800px)}
.hex-a{background:linear-gradient(160deg,#b9b9b9,#5c5c5c);clip-path:polygon(325px 638px,417px 638px,455px 733px,417px 830px,325px 830px,282px 733px)}
.hex-b{background:linear-gradient(160deg,#d0d0d0,#6f6f6f);clip-path:polygon(462px 748px,528px 748px,560px 806px,528px 862px,462px 862px,432px 806px)}
.cover-brand{position:absolute;left:30px;top:50px;font-weight:700;font-size:46px;line-height:44px;color:var(--ink)}
.cover-text{position:absolute;right:26px;text-align:right;color:#fff}
.cover-title{top:108px;font-size:45px;font-weight:700;line-height:52px}
.cover-title::after{content:"";display:block;width:94px;height:3px;background:#fff;margin:16px 0 0 auto}
.cover-sub{top:250px;font-size:16px;font-weight:700}
.cover-block h3{font-size:16px;font-weight:700;line-height:22px}
.cover-block p{font-size:15px;line-height:18.5px}
.cover-project{top:333px;width:290px}
.cover-client{top:448px;width:260px}
.cover-ref{top:570px;font-size:16px;font-weight:700}
.cover-web{position:absolute;left:12px;top:844px;font-size:9px;letter-spacing:5.6px;color:var(--ink);font-weight:600;text-transform:uppercase}

/* revision */
.revision{position:absolute;left:40px;top:205px;width:542px;border-collapse:collapse;font-size:12px;color:var(--text);table-layout:fixed}
.revision td,.revision th{height:19.5px;border-right:1px solid #fff;text-align:center;font-weight:400;padding:0}
.revision th{background:var(--yellow);color:var(--ink);font-weight:600;border-top:2px solid var(--rule)}
.revision tr.band td{background:var(--yellow-soft)}
.revision .small{font-size:8.5px}
.box{display:inline-block;width:12px;height:12px;border:1px solid var(--ink);vertical-align:-2px;margin-left:4px}
.box.checked{background:radial-gradient(var(--ink) 45%,transparent 50%)}
.ghost{position:absolute;left:40px;top:410px;width:540px;text-align:center;font-weight:700;color:var(--ghost);font-size:96px;line-height:130px;white-space:nowrap}
.fineprint{position:absolute;left:24px;top:825px;width:550px;font-size:6.5px;font-style:italic;color:#666;line-height:8px}

/* contents */
.toc{position:absolute;left:45px;top:182px;width:527px;list-style:none;font-size:12px;color:var(--ink)}
.toc li{display:flex;height:21.7px;align-items:center;text-transform:uppercase}
.toc li .lead{flex:1;border-bottom:1px dotted #777;margin:0 4px;transform:translateY(3px)}
.toc .l1{font-weight:700}
.toc .l2{padding-left:28px}
.toc .l3{padding-left:50px;text-transform:none}

/* body */
.body{position:absolute;left:36px;width:556px;font-size:12.5px;line-height:15px;color:var(--text)}
.body p{margin-bottom:15px}
.body ul{list-style:none;margin-bottom:15px}
.body li{padding-left:14px;position:relative}
.body li::before{content:"•";position:absolute;left:0}
.body strong{font-weight:700;color:var(--ink)}
.justified{text-align:justify}
.chart{position:absolute;left:130px;top:180px}
.divider{position:absolute;left:369px;top:614px;width:2px;height:216px;background:var(--ink)}
.donut{position:absolute;left:92px;top:622px}
.pct{position:absolute;font-size:27px;font-weight:600;color:var(--ink);line-height:30px}
.side-note{position:absolute;left:396px;top:642px;width:196px;font-size:12.5px;line-height:22px;color:var(--text)}
</style>
</head>
<body>

<!-- Cover -->
<section class="page p1 cover">
  <div class="cover-shape cover-top"></div>
  <div class="cover-shape cover-photo" role="img" aria-label="Photo of a technician in a yellow coat handling sample tins on laboratory shelving"></div>
  <div class="cover-shape hex-a" role="img" aria-label="Photo of a construction site with a drilling rig and city skyline"></div>
  <div class="cover-shape hex-b" role="img" aria-label="Photo of laboratory microscope equipment"></div>
  <div class="cover-shape cover-bottom"></div>
  <div class="cover-brand">TARNVALE<br>CORES</div>
  <h1 class="cover-text cover-title">YOUR HEADING<br>GOES HERE</h1>
  <div class="cover-text cover-sub">Subtitle goes here</div>
  <div class="cover-text cover-block cover-project"><h3>Project goes here</h3><p>Lorem ipsum dolor sit amet, consectetuer adipiscing elit, sed diam nonummy nibh euismod tincidunt</p></div>
  <div class="cover-text cover-block cover-client"><h3>Client name goes here</h3><p>Lorem ipsum dolor sit amet, consec­tetuer adipiscing elit, sed diam nonummy</p></div>
  <div class="cover-text cover-ref">Reference number goes here</div>
  <div class="cover-web">www.tarnvalecores.com</div>
</section>

<!-- Revision table -->
<section class="page p2">
  <svg class="edge" viewBox="0 0 10 869" aria-hidden="true"><polygon points="0,0 10,0 10,455 0,465" fill="var(--yellow)"/><polygon points="0,465 10,455 10,869 0,869" fill="var(--ink)"/></svg>
  <div class="brand">TARNVALE<span>CORES</span></div>
  <div class="ghost">TARNVALE<br>CORES</div>
  <div class="pill" style="top:108px">REVISION TABLE</div>
  <table class="revision">
    <tr><th>REV</th><th>DATE</th><th>DETAILS</th><th>CHECKED</th><th>APPROVED</th></tr>
    <tr><td></td><td></td><td></td><td>D&amp;G Dept. Mgr</td><td>General Manager</td></tr>
    <tr class="band"><td></td><td></td><td></td><td></td><td></td></tr>
    <tr><td>1</td><td>10-Nov-19</td><td>Draft plan</td><td>KPAM</td><td>AJS</td></tr>
    <tr class="band"><td>2</td><td></td><td></td><td></td><td></td></tr>
    <tr><td></td><td></td><td></td><td class="small">COPY NO.</td><td></td></tr>
    <tr class="band"><td></td><td></td><td></td><td class="small">CONTROLLED COPY</td><td>YES<span class="box"></span>&nbsp;&nbsp;&nbsp;&nbsp;&nbsp;&nbsp;NO<span class="box checked"></span></td></tr>
  </table>
  <p class="fineprint">Lorem ipsum dolor sit amet, consectetuer adipiscing elit, sed diam nonummy nibh euismod tincidunt ut laoreet dolore magna aliquam erat volutpat ut wisi enim.</p>
  <div class="footer-rule"></div><div class="folio">2</div>
</section>

<!-- Contents -->
<section class="page p3">
  <svg class="edge" viewBox="0 0 10 869" aria-hidden="true"><polygon points="0,0 10,0 10,410 0,420" fill="var(--yellow)"/><polygon points="0,420 10,410 10,869 0,869" fill="var(--ink)"/></svg>
  <div class="brand">TARNVALE<span>CORES</span></div>
  <div class="pill" style="top:108px">TABLE OF CONTENTS</div>
  <ol class="toc">
    <li class="l1">01. Introduction<span class="lead"></span>2</li>
    <li class="l1">02. Project overview<span class="lead"></span>2</li>
    <li class="l2">2.1. Company overview<span class="lead"></span>2</li>
    <li class="l2">2.2. LIMS overview<span class="lead"></span>3</li>
    <li class="l2">2.3. Hardware and operating system overview<span class="lead"></span>3</li>
    <li class="l3">2.3.1 Direct links to instruments/systems<span class="lead"></span>3</li>
    <li class="l3">2.3.2 Interfaces with other software<span class="lead"></span>4</li>
    <li class="l2">2.4. Database overview<span class="lead"></span>4</li>
    <li class="l1">03. LIMS technical requirements<span class="lead"></span>5</li>
    <li class="l2">3.1. Sample registration<span class="lead"></span>5</li>
    <li class="l2">3.2. Labelling<span class="lead"></span>6</li>
    <li class="l2">3.3. Test program (TP)<span class="lead"></span>7</li>
    <li class="l2">3.4. Electronic worksheets and calculations<span class="lead"></span>8</li>
    <li class="l2">3.5. Workflows<span class="lead"></span>9</li>
    <li class="l2">3.6. Acquiring analytical results<span class="lead"></span>10</li>
    <li class="l2">3.7. Sample tracking<span class="lead"></span>11</li>
    <li class="l2">3.8. Data validation and approval<span class="lead"></span>11</li>
    <li class="l2">3.9. Technical reporting<span class="lead"></span>12</li>
    <li class="l2">3.10. Data management<span class="lead"></span>13</li>
    <li class="l2">3.11. Number of concurrent users<span class="lead"></span>13</li>
    <li class="l2">3.12. Security<span class="lead"></span>14</li>
    <li class="l2">3.13. Tables of reference information<span class="lead"></span>15</li>
    <li class="l1">04. LIMS business management requirements<span class="lead"></span>16</li>
    <li class="l2">4.1. Management access<span class="lead"></span>16</li>
    <li class="l2">4.2. Client access<span class="lead"></span>17</li>
    <li class="l2">4.3. Business reporting<span class="lead"></span>17</li>
    <li class="l1">Appendix A Laboratories process flow<span class="lead"></span>18</li>
    <li class="l1">Appendix B Instrument list with network connectivity<span class="lead"></span>19</li>
    <li class="l1">Appendix C List of tests<span class="lead"></span>20</li>
  </ol>
  <div class="footer-rule"></div><div class="folio">3</div>
</section>

<!-- Introduction -->
<section class="page p4">
  <svg class="edge" viewBox="0 0 10 869" aria-hidden="true"><polygon points="0,0 10,0 10,410 0,420" fill="var(--yellow)"/><polygon points="0,420 10,410 10,869 0,869" fill="var(--ink)"/></svg>
  <div class="brand">TARNVALE<span>CORES</span></div>
  <div class="pill numbered" style="top:106px"><span class="num">01</span>INTRODUCTION</div>
  <div class="body" style="top:180px">
    <p>The purpose of this Stakeholder Management Plan is to define the requirements, processes, and techniques for engaging stakeholders based on an analysis of their needs, interests, and abilities to impact the project.</p>
    <p>The objectives of the Stakeholder Management Plan are to document and communicate how information will be disseminated to, and received from all stakeholders connected with the project.<br>The SMP shall therefore:</p>
    <ul>
      <li>Identify who the stakeholders are</li>
      <li>Establish the requirements of each stakeholder</li>
      <li>The requirements of the project to receive information and/or obtain approvals from stakeholders</li>
      <li>Analyse the power and interest of each stakeholder</li>
      <li>Define the means and frequency of communication with each stakeholder</li>
    </ul>
  </div>
  <div class="pill numbered" style="top:411px"><span class="num">02</span>IDENTIFYING STAKEHOLDERS</div>
  <div class="body justified" style="top:483px">
    <p>As part of the project planning process, the project management team shall identity potential stakeholders against the following criteria:</p>
    <ul style="text-align:left">
      <li>Will the person or their organization be directly or indirectly affected by this project?</li>
      <li>Does the person or their organization hold a position from which they can influence the project?</li>
      <li>Does the person have an impact on the project’s resources (material, personnel, funding)?</li>
      <li>Does the person or their organization have any special skills or capabilities the project will require?</li>
      <li>Does the person potentially benefit from the project or are they in a position to resist this change?</li>
    </ul>
    <p>Stakeholders may include BOTH internal and external personnel or organisations.</p>
    <p><strong>Internal stakeholders</strong> might include the project team, including contractors and vendors, as well as top management, resourcing directors, accounting department members, and others who want to see the project run efficiently and profitably.</p>
    <p><strong>External stakeholders</strong> are individuals or groups outside the organization who could be impacted by the project or those who govern policy that influences and could affect the project. Such groups might include the client, regulatory bodies, vendors, etc. Besides identifying and classifying all stakeholders, it is important to include everyone who will be even tangentially impacted by the project.</p>
    <p style="margin:0">Once identified, all Stakeholders shall be recorded in the Stakeholder Management Register.<br><em>(See Appendix A)</em></p>
  </div>
  <div class="footer-rule"></div><div class="folio">4</div>
</section>

<!-- Figures -->
<section class="page p5">
  <svg class="edge" viewBox="0 0 10 869" aria-hidden="true"><polygon points="0,0 10,0 10,410 0,420" fill="var(--yellow)"/><polygon points="0,420 10,410 10,869 0,869" fill="var(--ink)"/></svg>
  <div class="brand">TARNVALE<span>CORES</span></div>
  <div class="pill numbered" style="top:106px"><span class="num">05</span>FIGURE WITH CAPTION / CHARTS</div>
  <svg class="chart" width="345" height="205" viewBox="0 0 345 205" role="img" aria-label="Bar chart with five alternating yellow and black bars">
    <g stroke="#dcdcdc" stroke-width="1">
      <line x1="0" y1="2" x2="345" y2="2"/><line x1="0" y1="22" x2="345" y2="22"/><line x1="0" y1="42" x2="345" y2="42"/><line x1="0" y1="62" x2="345" y2="62"/><line x1="0" y1="82" x2="345" y2="82"/><line x1="0" y1="102" x2="345" y2="102"/><line x1="0" y1="122" x2="345" y2="122"/><line x1="0" y1="142" x2="345" y2="142"/><line x1="0" y1="162" x2="345" y2="162"/><line x1="0" y1="182" x2="345" y2="182"/>
    </g>
    <line x1="1" y1="0" x2="1" y2="203" stroke="#999"/><line x1="0" y1="203" x2="345" y2="203" stroke="#999"/>
    <rect x="38" y="143" width="42" height="60" fill="var(--yellow)"/>
    <rect x="94" y="116" width="43" height="87" fill="var(--ink)"/>
    <rect x="151" y="72" width="42" height="131" fill="var(--yellow)"/>
    <rect x="208" y="101" width="42" height="102" fill="var(--ink)"/>
    <rect x="264" y="86" width="42" height="117" fill="var(--yellow)"/>
  </svg>
  <div class="body" style="top:418px">
    <p>The purpose of this Stakeholder Management Plan is to define the requirements, processes, and techniques for engaging stakeholders based on an analysis of their needs, interests, and abilities to impact the project.</p>
    <p>The objectives of the Stakeholder Management Plan are to document and communicate how information will be disseminated to, and received from all stakeholders connected with the project.<br>The SMP shall therefore:</p>
    <ul>
      <li>Identify who the stakeholders are</li>
      <li>Establish the requirements of each stakeholder</li>
      <li>The requirements of the project to receive information and/or obtain approvals from stakeholders</li>
      <li>Analyse the power and interest of each stakeholder</li>
      <li>Define the means and frequency of communication with each stakeholder</li>
    </ul>
  </div>
  <svg class="donut" width="200" height="200" viewBox="0 0 200 200" role="img" aria-label="Donut chart, 25% and 75%">
    <circle cx="98" cy="100" r="68" fill="none" stroke="var(--yellow)" stroke-width="34" stroke-dasharray="262 427" stroke-dashoffset="-161" transform="rotate(-90 98 100)"/>
    <circle cx="98" cy="100" r="68" fill="none" stroke="var(--ink)" stroke-width="34" stroke-dasharray="155 427" stroke-dashoffset="-4" transform="rotate(-90 98 100)"/>
  </svg>
  <div class="pct" style="left:286px;top:645px">25%</div>
  <div class="pct" style="left:66px;top:772px">75%</div>
  <div class="divider"></div>
  <p class="side-note">Lorem ipsum dolor sit amet, consec­tetuer adipiscing elit, sed diam nonummy nibh euismod tincidunt ut laoreet dolore magna aliquam erat volutpat. Ut wisi enim ad minim veniam, quis nostrud exerci tation ullamcorper suscipit lobortis nisl ut</p>
  <div class="footer-rule"></div><div class="folio">10</div>
</section>

<!-- Appendices -->
<section class="page p6">
  <svg class="edge" viewBox="0 0 10 869" aria-hidden="true"><polygon points="0,0 10,0 10,410 0,420" fill="var(--yellow)"/><polygon points="0,420 10,410 10,869 0,869" fill="var(--ink)"/></svg>
  <div class="brand">TARNVALE<span>CORES</span></div>
  <div class="pill dark" style="top:106px">APPENDIX A</div>
  <div class="body justified" style="top:165px">
    <p style="margin:0">Lorem ipsum dolor sit amet, consectetuer adipiscing elit, sed diam nonummy nibh euismod tincidunt ut laoreet dolore magna aliquam erat volutpat. Ut wisi enim ad minim veniam, quis nostrud exerci tation ullamcorper suscipit lobortis nisl ut aliquip ex ea commodo consequat. Duis autem vel eum iriure dolor in hendrerit in vulputate velit esse molestie consequat, vel illum dolore eu feugiat nulla facilisis at vero eros et accumsan et iusto odio dignissim qui blandit praesent luptatum zzril delenit augue duis dolore te feugait nulla facilisi.<br>Lorem ipsum dolor sit amet, cons ectetuer adipiscing elit, sed diam nonummy nibh euismod tincidunt ut laoreet dolore magna aliquam erat volutpat. Ut wisi enim ad minim veniam, quis nostrud exerci tation ullamcorper suscipit lobortis nisl ut aliquip ex ea commodo consequat.<br>Lorem ipsum dolor sit amet, consectetuer adipiscing elit, sed diam nonummy nibh euismod tincidunt ut laoreet dolore magna aliquam erat volutpat. Ut wisi enim ad minim veniam, quis nostrud</p>
  </div>
  <div class="pill dark" style="top:357px">APPENDIX B</div>
  <div class="body justified" style="top:423px">
    <p style="margin:0">Lorem ipsum dolor sit amet, consectetuer adipiscing elit, sed diam nonummy nibh euismod tincidunt ut laoreet dolore magna aliquam erat volutpat. Ut wisi enim ad minim veniam, quis nostrud exerci tation ullamcorper suscipit lobortis nisl ut aliquip ex ea commodo consequat. Duis autem vel eum iriure dolor in hendrerit in vulputate velit esse molestie consequat, vel illum dolore eu feugiat nulla facilisis at vero eros et accumsan et iusto odio dignissim qui blandit praesent luptatum zzril delenit augue duis dolore te feugait nulla facilisi.<br>Lorem ipsum dolor sit amet, cons ectetuer adipiscing elit, sed diam nonummy nibh euismod tincidunt ut laoreet dolore magna aliquam erat volutpat. Ut wisi enim ad minim veniam, quis nostrud exerci tation ullamcorper suscipit lobortis nisl ut aliquip ex ea commodo consequat.<br>Lorem ipsum dolor sit amet, consectetuer adipiscing elit, sed diam nonummy nibh euismod tincidunt ut laoreet dolore magna aliquam erat volutpat. Ut wisi enim ad minim veniam, quis nostrud</p>
  </div>
  <div class="pill dark" style="top:608px;left:20px;right:22px">APPENDIX C</div>
  <div class="body justified" style="top:672px;left:33px">
    <p>Lorem ipsum dolor sit amet, consectetuer adipiscing elit, sed diam nonummy nibh euismod tincidunt ut laoreet dolore magna aliquam erat volutpat. Ut wisi enim ad minim veniam, quis nostrud exerci tation ullamcorper suscipit lobortis nisl ut aliquip ex ea commodo consequat. Duis autem vel eum iriure dolor in hendrerit in vulputate velit esse molestie consequat, vel illum dolore eu feugiat nulla facilisis at vero eros et accumsan et iusto odio dignissim qui blandit praesent luptatum zzril delenit augue duis dolore te feugait nulla facilisi.</p>
    <p style="text-align:left">Lorem ipsum dolor sit amet, cons ectetuer adipiscing elit, sed diam nonummy nibh euismod tincidunt ut laoreet dolore magna a</p>
  </div>
  <div class="footer-rule"></div><div class="folio">20</div>
</section>

</body>
</html>
```